Business Cards and label design needed!

I am a metalsmith, working in sterling silver, brass and moving slowly into adding some gold accent pieces. I also use patinas to add color to brass pieces. The peacock feather is used in my packaging, as both a label and tissue paper. I am attaching what I am currently using, and printing at home, but I need a design that I can have professionally printed. My website is www.fernhollowworks.com
Target Market(s)
Established Professionals, Independent thinkers, Art donors, Artist supporters
Industry/Entity Type
Jewelry
Contact Information for Business Card
I would like a business card with the basic contact information, including Facebook and Instagram. I currently use a peacock feather and would like to continue that. I like to use turquoise, Tiffany blue and colors in that direction. I am open to other suggestions. I would like to be able to transfer the design to oval labels as well.
Other font styles liked:
- Garamond or other fonts that have a slight script that is easy to read
Look and feel

```html
<!DOCTYPE html>
<html lang="en">
<head>
<meta charset="utf-8">
<title>Fern Hollow Works — Business Card</title>
<link rel="stylesheet" href="https://fonts.googleapis.com/css2?family=Work+Sans:wght@400;500;600&display=swap">
<style>
  :root {
    --page: #2b2b2b;
    --indigo: #2d3894;
    --teal: #1f9a96;
    --white: #ffffff;
    --rule: #3a44a0;
  }
  * { box-sizing: border-box; margin: 0; padding: 0; }
  html, body { width: 1200px; height: 930px; overflow: hidden; }
  body {
    background: var(--page);
    font-family: "Work Sans", sans-serif;
    position: relative;
  }
  .card {
    position: absolute;
    width: 620px;
    height: 354px;
    overflow: hidden;
    box-shadow: 0 10px 24px rgba(0,0,0,.45);
  }

  /* Front */
  .card-front {
    left: 60px; top: 60px;
    background: var(--indigo);
  }
  .front-map {
    position: absolute;
    left: 70px; top: 50px;
    width: 480px; height: 250px;
    border-radius: 40px;
    background: radial-gradient(ellipse at center, rgba(120,135,210,.32), rgba(45,56,148,0) 70%);
  }
  .front-brand {
    position: absolute;
    left: 0; right: 0; top: 152px;
    display: flex; align-items: center; justify-content: center; gap: 14px;
    color: var(--white);
    font-weight: 400;
    font-size: 38px;
    letter-spacing: 1px;
  }
  .front-brand .mark {
    width: 22px; height: 22px; border-radius: 50%;
    background: var(--teal);
  }

  /* Back */
  .card-back {
    left: 520px; top: 500px;
    background: var(--white);
  }
  .back-brand {
    position: absolute;
    left: 44px; top: 116px;
    display: flex; align-items: center; gap: 12px;
    color: var(--indigo);
    font-weight: 400;
    font-size: 28px;
    letter-spacing: .5px;
  }
  .back-brand .mark {
    width: 18px; height: 18px; border-radius: 50%;
    background: var(--teal);
  }
  .holder {
    position: absolute;
    right: 48px; top: 46px;
    text-align: right;
  }
  .holder-name {
    color: var(--indigo);
    font-weight: 600;
    font-size: 23px;
    letter-spacing: .2px;
  }
  .holder-title {
    color: var(--teal);
    font-size: 14px;
    margin-top: 1px;
  }
  .holder-rule {
    position: absolute;
    left: 330px; right: 48px; top: 98px;
    height: 1.5px;
    background: var(--rule);
  }
  .rule {
    position: absolute;
    left: 110px; right: 160px; top: 204px;
    height: 1.5px;
    background: var(--rule);
  }
  .location {
    position: absolute;
    right: 40px; top: 166px;
    color: var(--teal);
    font-size: 14px;
  }
  .contacts {
    position: absolute;
    left: 112px; top: 226px;
    list-style: none;
    color: var(--teal);
    font-size: 15.5px;
    line-height: 23px;
  }
  .contacts li { display: flex; align-items: center; gap: 8px; }
  .contacts svg { width: 11px; height: 11px; fill: none; stroke: var(--indigo); stroke-width: 1.6; }
  .swoosh { position: absolute; left: 0; top: 0; }
</style>
</head>
<body>

  <section class="card card-front" aria-label="Card front">
    <div class="front-map" role="img" aria-label="Faint dotted world map decoration"></div>
    <div class="front-brand"><span class="mark"></span>Fern Hollow Works</div>
  </section>

  <section class="card card-back" aria-label="Card back">
    <svg class="swoosh" width="620" height="354" viewBox="0 0 620 354" aria-hidden="true">
      <path d="M330 354 C 400 300, 500 230, 620 205 L 620 354 Z" fill="var(--teal)"/>
      <path d="M372 354 C 440 300, 520 245, 620 222 L 620 354 Z" fill="var(--white)"/>
      <path d="M378 354 C 445 303, 525 250, 620 228 L 620 354 Z" fill="var(--indigo)"/>
    </svg>

    <div class="holder">
      <div class="holder-name">DANIEL REEVE</div>
      <div class="holder-title">Director</div>
    </div>
    <div class="holder-rule"></div>

    <div class="back-brand"><span class="mark"></span>Fern Hollow Works</div>

    <div class="location">Marlow Falls, TX 76000</div>
    <div class="rule"></div>

    <ul class="contacts">
      <li>
        <svg viewBox="0 0 12 12"><path d="M2 1.5 L4.5 1.5 L5.3 4 L4 5 C4.7 6.6 5.6 7.5 7 8 L8 6.7 L10.5 7.5 L10.5 10 C6 10.3 1.7 6 2 1.5 Z"/></svg>
        555-014-2297
      </li>
      <li>
        <svg viewBox="0 0 12 12"><rect x="1" y="2.5" width="10" height="7"/><path d="M1 2.5 L6 6.5 L11 2.5"/></svg>
        designsbyfernhollow@mailbox.com
      </li>
      <li>
        <svg viewBox="0 0 12 12"><circle cx="6" cy="6" r="5"/><path d="M1 6 H11 M6 1 C3.5 3.5 3.5 8.5 6 11 M6 1 C8.5 3.5 8.5 8.5 6 11"/></svg>
        www.fernhollowworks.com
      </li>
    </ul>
  </section>

</body>
</html>
```